RM Tomás Rivera (Business Card)

Hi designers, in this work, I'm looking for an sophisticated stylish, elegant and proffesional personal card. We have a laboratory of pathology automated, with equipments high quality.
In this web the designers, have created my business logo, the name is "RM Tomás Rivera"
In our lab, we principal work is to prepare the biopsies for further diagnostic of diseases like cancer, tumors, etc.
I need that the first face, only having my complete logo (Rm Tomás Rivera, Laboratorio de procesamiento Histologico)
The overleaf, could repeat the same logo, like water logo.
In this face, I need to say: My full data:

Técnico en Anatomía Patológica
Tomás Rivera Ibarra M.P 47203
Av. Paredes Luján 418 - 2do piso - Instituto Marbel.
Córdoba, Argentina
(0351) 154820937
rivera.tomas@correolab.example

with respect the colors of card, use your imagination, the original logo color is violet, I haven't chosen a color base for the card.

attached pictures are examples of cards I like your DESIGN.
Attached too, the original logo to my company.

the size of card are:
horizontal: 9cm
vertical: 5,5cm

any question that you have, not doubt to question me,
Hand to work!

Industry/Entity Type

Laboratory

Requirements
Must have
• designers sophisticated, not simples, like show the images attached

```html
<!DOCTYPE html>
<html lang="es">
<head>
<meta charset="utf-8">
<title>RM Tomás Rivera — Tarjeta personal</title>
<link rel="stylesheet" href="https://fonts.googleapis.com/css2?family=Roboto:wght@400;500;700&family=Roboto+Condensed:wght@400;500&display=swap">
<style>
  :root {
    --violet: #6a2c9e;
    --violet-deep: #55207f;
    --violet-light: #8a4cc4;
    --ink: #3a3a3c;
    --grey: #5d5d60;
    --grey-line: #a9a9ad;
    --paper: #ffffff;
    --backdrop: #e9e8ec;
  }
  * { margin: 0; padding: 0; box-sizing: border-box; }
  html, body { width: 1200px; height: 900px; overflow: hidden; }
  body {
    background: var(--backdrop);
    font-family: "Roboto", Arial, sans-serif;
    display: flex;
    flex-direction: column;
    align-items: center;
    justify-content: center;
    gap: 30px;
  }
  .card {
    position: relative;
    width: 660px;
    height: 403px;
    background: var(--paper);
    overflow: hidden;
    box-shadow: 0 6px 18px rgba(40, 20, 60, 0.18);
  }
  .card-art { position: absolute; inset: 0; width: 100%; height: 100%; }

  /* Logo lockup */
  .brand { position: absolute; display: flex; flex-direction: column; align-items: center; }
  .brand-mark { background: var(--violet); }
  .brand-name {
    font-family: "Roboto Condensed", "Arial Narrow", sans-serif;
    font-weight: 400;
    color: var(--grey);
    text-transform: uppercase;
    letter-spacing: 0.32em;
    white-space: nowrap;
  }
  .brand-rule { background: var(--grey); height: 1px; }
  .brand-tagline {
    font-family: "Roboto Condensed", "Arial Narrow", sans-serif;
    font-weight: 400;
    color: var(--grey);
    text-transform: uppercase;
    white-space: nowrap;
  }

  /* Back face */
  .card--contact .brand { top: 22px; left: 170px; }
  .card--contact .brand-mark { width: 30px; height: 30px; margin-bottom: 6px; }
  .card--contact .brand-name { font-size: 13px; }
  .card--contact .brand-rule { width: 240px; margin: 3px 0; }
  .card--contact .brand-tagline { font-size: 13px; }

  .contact {
    position: absolute;
    right: 36px;
    top: 114px;
    text-align: right;
  }
  .contact-role { font-size: 15px; font-weight: 700; color: var(--violet); line-height: 18px; }
  .contact-name { font-size: 27px; font-weight: 700; color: var(--ink); margin-top: 4px; line-height: 32px; letter-spacing: -0.01em; }
  .contact-details {
    list-style: none;
    margin-top: 42px;
    font-size: 15px;
    line-height: 1.62;
    color: var(--paper);
    white-space: nowrap;
  }

  /* Front face */
  .card--front .brand { top: 108px; left: 0; right: 0; }
  .card--front .brand-mark { width: 64px; height: 64px; margin-bottom: 12px; }
  .card--front .brand-name { font-size: 24px; }
  .card--front .brand-rule { width: 380px; margin: 6px 0 8px; }
  .card--front .brand-tagline { font-size: 27px; letter-spacing: 0.01em; }
</style>
</head>
<body>

  <!-- Front face: logo only -->
  <section class="card card--front" aria-label="Tarjeta, frente">
    <svg class="card-art" viewBox="0 0 660 403" aria-hidden="true">
      <path d="M0,0 H660 V92 C520,44 300,30 0,52 Z" fill="var(--violet)"/>
      <path d="M0,52 C300,30 520,44 660,92" fill="none" stroke="var(--violet-light)" stroke-width="4"/>
      <path d="M0,66 C300,40 520,56 660,104" fill="none" stroke="var(--grey-line)" stroke-width="3"/>
      <path d="M0,300 C140,352 400,356 660,318 V403 H0 Z" fill="var(--violet)"/>
      <path d="M0,336 C200,384 420,372 660,340 V403 H0 Z" fill="var(--violet-deep)"/>
      <path d="M0,290 C140,342 400,346 660,308" fill="none" stroke="var(--grey-line)" stroke-width="3"/>
      <path d="M40,352 C240,392 460,378 660,350" fill="none" stroke="var(--paper)" stroke-width="2" opacity="0.6"/>
    </svg>
    <div class="brand">
      <span class="brand-mark"></span>
      <span class="brand-name">RM Tomás Rivera</span>
      <span class="brand-rule"></span>
      <span class="brand-tagline">Laboratorio de procesamiento histologico</span>
    </div>
  </section>

  <!-- Back face: contact data -->
  <section class="card card--contact" aria-label="Tarjeta, dorso">
    <svg class="card-art" viewBox="0 0 660 403" aria-hidden="true">
      <path d="M0,218 C220,206 440,192 660,178 V403 H0 Z" fill="var(--violet)"/>
      <path d="M120,403 C260,330 460,250 660,226 V290 C480,310 320,360 250,403 Z" fill="var(--violet-light)" opacity="0.55"/>
      <path d="M0,211 C220,199 440,185 660,171" fill="none" stroke="var(--violet)" stroke-width="2"/>
      <path d="M0,330 C180,300 360,290 520,300" fill="none" stroke="var(--paper)" stroke-width="1.5" opacity="0.35"/>
    </svg>
    <div class="brand">
      <span class="brand-mark"></span>
      <span class="brand-name">RM Tomás Rivera</span>
      <span class="brand-rule"></span>
      <span class="brand-tagline">Laboratorio de procesamiento histologico</span>
    </div>
    <div class="contact">
      <p class="contact-role">Técnico en Anatomía Patológica</p>
      <p class="contact-name">Tomás Rivera Ibarra M.P 47203</p>
      <ul class="contact-details">
        <li>Av. Paredes Luján 418 - 2do piso - Instituto Marbel</li>
        <li>Córdoba, Argentina</li>
        <li>(0351) 154820937</li>
        <li>rivera.tomas@correolab.example</li>
      </ul>
    </div>
  </section>

</body>
</html>
```